Business Card For Kelmora Financial Consulting

Hi, I would like a business card designed. Bold, modern.
Please use the same design as the logo. I have also attached the website design to see the overall theme.
Wordmark Font
Color: Hex: #01AEF7

```html
<!DOCTYPE html>
<html lang="en">
<head>
<meta charset="utf-8">
<title>Kelmora Financial Consulting – Business Card</title>
<link href="https://fonts.googleapis.com/css2?family=Open+Sans:wght@400;600;700&display=swap" rel="stylesheet">
<style>
  :root {
    --brand-blue: #01AEF7;
    --ink: #000000;
    --paper-white: #ffffff;
    --backdrop: #1b1b1b;
  }
  * { margin: 0; padding: 0; box-sizing: border-box; }
  html, body {
    width: 1200px; height: 800px; overflow: hidden;
    background: var(--backdrop);
    font-family: "Open Sans", sans-serif;
  }
  .canvas { position: relative; width: 1200px; height: 800px; }

  .card { position: absolute; overflow: hidden; }

  /* Front */
  .card-front {
    left: 381px; top: 131px; width: 455px; height: 257px;
    background: var(--brand-blue);
  }
  .front-band { position: absolute; left: 0; top: 85px; width: 240px; height: 98px; }
  .front-wordmark {
    position: absolute; left: 14px; top: 122px;
    display: flex; align-items: center; gap: 8px;
  }
  .brand-square {
    width: 16px; height: 16px; background: var(--brand-blue); flex: none;
  }
  .brand-name {
    color: var(--paper-white); font-weight: 600; font-size: 12.5px;
    letter-spacing: 0.3px; white-space: nowrap;
  }
  .person-name {
    position: absolute; left: 247px; top: 81px;
    font-size: 19px; font-weight: 700; color: var(--ink); white-space: nowrap;
  }
  .person-role {
    position: absolute; left: 243px; top: 105px;
    font-size: 13px; color: var(--ink);
  }
  .contact-line {
    position: absolute; display: flex; align-items: center; gap: 5px;
    font-size: 12.5px; color: var(--ink); white-space: nowrap;
  }
  .contact-line svg { width: 10px; height: 10px; flex: none; }
  .contact-phone { left: 237px; top: 137px; }
  .contact-email { left: 230px; top: 154px; }
  .contact-web   { left: 225px; top: 171px; }

  /* Back */
  .card-back {
    left: 382px; top: 420px; width: 452px; height: 249px;
    background: var(--ink);
  }
  .back-wordmark {
    position: absolute; left: 0; right: 0; top: 104px;
    display: flex; justify-content: center; align-items: center; gap: 10px;
  }
  .back-wordmark .brand-square { width: 24px; height: 24px; }
  .back-wordmark .brand-name { font-size: 19px; }
  .back-url {
    position: absolute; left: 0; right: 0; top: 199px; text-align: center;
    font-size: 13px; font-weight: 700; color: var(--paper-white);
  }
  .back-url .url-domain { color: var(--brand-blue); font-weight: 600; }
</style>
</head>
<body>
<main class="canvas">

  <section class="card card-front" aria-label="Business card front">
    <svg class="front-band" viewBox="0 0 240 98" aria-hidden="true">
      <polygon points="0,0 240,0 217,97 0,98" fill="var(--ink)"/>
    </svg>
    <div class="front-wordmark">
      <span class="brand-square"></span>
      <span class="brand-name">Kelmora Financial Consulting</span>
    </div>

    <h1 class="person-name">Daniel Harrow</h1>
    <p class="person-role">CEO</p>

    <p class="contact-line contact-phone">
      <svg viewBox="0 0 10 10" aria-hidden="true"><path d="M2 0.5 L3.6 2.6 L2.7 3.6 Q3.8 5.9 6.3 7.2 L7.4 6.3 L9.5 7.9 L8.4 9.5 Q1.5 8.3 0.5 1.6 Z" fill="var(--ink)"/></svg>
      555 0142 736
    </p>
    <p class="contact-line contact-email">
      <svg viewBox="0 0 10 10" aria-hidden="true"><rect x="0.5" y="2" width="9" height="6" fill="var(--ink)"/><path d="M0.5 2 L5 5.5 L9.5 2" stroke="var(--brand-blue)" stroke-width="0.8" fill="none"/></svg>
      Daniel@kelmoraconsulting.com
    </p>
    <p class="contact-line contact-web">
      <svg viewBox="0 0 10 10" aria-hidden="true"><g fill="none" stroke="var(--ink)" stroke-width="0.9"><circle cx="5" cy="5" r="4.3"/><ellipse cx="5" cy="5" rx="1.8" ry="4.3"/><line x1="0.7" y1="5" x2="9.3" y2="5"/></g></svg>
      www.kelmoraconsulting.com
    </p>
  </section>

  <section class="card card-back" aria-label="Business card back">
    <div class="back-wordmark">
      <span class="brand-square"></span>
      <span class="brand-name">Kelmora Financial Consulting</span>
    </div>
    <p class="back-url">www.<span class="url-domain">kelmoraconsulting</span>.com</p>
  </section>

</main>
</body>
</html>
```